Rehearsal studio business card design needed

My rehearsal studio i bought not that long ago was opened as a hobby originally and was definitely not taken seriously. I am trying to make the new look studio be launched with the new look business cards. I am looking for very simple and clean look cards to match the simple and clean studios. the colour scheme is red and grey. over all i am really just looking for a very simple card that is not too busy and just gets the point accross.
Target Market(s)
Targeting bands, music teachers, students, etc.
Industry/Entity Type
Business
Contact Information for Business Card
Bayridge Sound Centre
Rehearsal and Recording Facilities
Owen Barlow CEO
unit 8, 47 Garvin Road Tallow NSW 2093
0491 382 905
bayridgesoundcentre@mailvex.com
Requirements
Must have
- simplicity
Nice to have

```html
<!DOCTYPE html>
<html lang="en">
<head>
<meta charset="utf-8">
<title>Bayridge Sound Centre – Business Card</title>
<link rel="stylesheet" href="https://fonts.googleapis.com/css2?family=Exo+2:wght@400;700&display=swap">
<style>
  :root {
    --backdrop: #2b2b2b;
    --card: #0b0b0b;
    --white: #f4f4f4;
    --grey: #b9b9b9;
    --red: #c8202a;
  }
  * { margin: 0; padding: 0; box-sizing: border-box; }
  html, body { width: 1200px; height: 900px; overflow: hidden; }
  body {
    background: var(--backdrop);
    font-family: "Exo 2", Arial, sans-serif;
    color: var(--white);
    position: relative;
  }
  .card {
    position: absolute;
    left: 280px;
    width: 640px;
    height: 366px;
    background: var(--card);
    box-shadow: 0 10px 30px rgba(0,0,0,.5);
  }
  .card--front { top: 62px; }
  .card--back { top: 472px; }

  .brand {
    display: flex;
    align-items: center;
    gap: 14px;
  }
  .brand__dot {
    flex: none;
    border-radius: 50%;
    background: var(--red);
  }
  .brand__name {
    font-weight: 700;
    color: var(--white);
    line-height: 1.05;
  }

  .card--front .brand {
    position: absolute;
    left: 150px;
    top: 150px;
  }
  .card--front .brand__dot { width: 56px; height: 56px; }
  .card--front .brand__name { font-size: 36px; }

  .back__heading {
    position: absolute;
    left: 40px;
    top: 32px;
    width: 560px;
    font-size: 21px;
    font-weight: 700;
    line-height: 1.2;
  }
  .back__heading .line2 { display: block; text-align: right; }

  .card--back .brand {
    position: absolute;
    left: 40px;
    top: 150px;
    width: 220px;
    flex-direction: column;
    text-align: center;
    gap: 12px;
  }
  .card--back .brand__dot { width: 90px; height: 90px; }
  .card--back .brand__name { font-size: 22px; }

  .divider {
    position: absolute;
    left: 300px;
    top: 120px;
    width: 2px;
    height: 200px;
    background: var(--red);
  }

  .contact {
    position: absolute;
    left: 330px;
    top: 124px;
    font-size: 15px;
    color: var(--grey);
    line-height: 1.3;
  }
  .contact__name {
    color: var(--red);
    font-size: 22px;
    text-transform: uppercase;
    line-height: 1.1;
  }
  .contact__role { font-size: 12px; margin-bottom: 18px; }
  .contact__address { margin-bottom: 18px; }
  .contact__email { white-space: nowrap; }
  .contact__email .accent { color: var(--red); }
</style>
</head>
<body>
  <section class="card card--front" aria-label="Card front">
    <div class="brand">
      <span class="brand__dot"></span>
      <span class="brand__name">Bayridge Sound Centre</span>
    </div>
  </section>

  <section class="card card--back" aria-label="Card back">
    <h1 class="back__heading">Bayridge Sound Centre Rehearsal <span class="line2">&amp; Recording Facilities</span></h1>

    <div class="brand">
      <span class="brand__dot"></span>
      <span class="brand__name">Bayridge Sound Centre</span>
    </div>

    <div class="divider"></div>

    <div class="contact">
      <p class="contact__name">Owen Barlow</p>
      <p class="contact__role">CEO</p>
      <p class="contact__address">Unit 8, 47 Garvin Road Tallow<br>NSW 2093</p>
      <p class="contact__phone">0491 382 905</p>
      <p class="contact__email"><span class="accent">bayridgesoundcentre</span>@mailvex.com</p>
    </div>
  </section>
</body>
</html>
```